TIDAL VERGE needs bisness cards pronto

Bisness name is "TIDAL VERGE" new bisness the bisness includes lawn mowing, garden matanace, and any jobs around the house.
I need a card that is colorful and vibrant and the bisness of lawn mowing maybe with some nature with it. It also needs my contact details"Darren Quellby mobile 0413562049 call for free quote and email norma.vance@fernmail.com.au and a catchy tag line

Industry/Entity Type

House

Requirements
Must have
• Bisness name "TIDAL VERGE"
Contact details "0413562049"
Email norma.vance@fernmail.com.au
Call for free quote

```html
<!DOCTYPE html>
<html lang="en">
<head>
<meta charset="utf-8">
<title>Tidal Verge – Business Card</title>
<link rel="stylesheet" href="https://fonts.googleapis.com/css2?family=Arimo:wght@400;700&display=swap">
<style>
  :root {
    --brand-blue: #1a6aa9;
    --wave-blue: #5b95cc;
    --sand: #b9aa9e;
    --card-white: #ffffff;
    --page: #e6e6e6;
  }
  * { margin: 0; padding: 0; box-sizing: border-box; }
  html, body {
    width: 781px;
    height: 1200px;
    overflow: hidden;
    background: var(--page);
    font-family: "Arimo", Arial, sans-serif;
  }
  .card {
    position: relative;
    width: 781px;
    height: 1200px;
    background: var(--card-white);
    border-radius: 28px;
    overflow: hidden;
  }
  .wave-band {
    position: absolute;
    top: 300px;
    left: 0;
    width: 100%;
    height: 340px;
    background: linear-gradient(170deg, var(--card-white) 0%, var(--sand) 45%, var(--wave-blue) 80%, var(--brand-blue) 100%);
  }
  .contact-panel {
    position: absolute;
    top: 640px;
    left: 0;
    width: 100%;
    height: 560px;
    background: var(--brand-blue);
  }
  .business-name {
    position: absolute;
    top: 158px;
    left: 64px;
    font-size: 84px;
    font-weight: 700;
    letter-spacing: 1px;
    color: var(--brand-blue);
    white-space: nowrap;
  }
  .owner-name {
    position: absolute;
    top: 710px;
    left: 90px;
    font-size: 52px;
    font-weight: 700;
    color: var(--card-white);
  }
  .contact-list {
    position: absolute;
    top: 855px;
    left: 120px;
    list-style: none;
    color: var(--card-white);
    font-size: 34px;
    font-weight: 700;
  }
  .contact-list li {
    display: flex;
    align-items: center;
    height: 62px;
  }
  .contact-icon {
    width: 40px;
    height: 36px;
    margin-right: 20px;
    flex: none;
  }
  .free-quote {
    position: absolute;
    top: 1016px;
    left: 0;
    width: 100%;
    text-align: center;
    font-size: 54px;
    font-weight: 700;
    color: var(--card-white);
  }
</style>
</head>
<body>
  <div class="card">
    <div class="wave-band" role="img" aria-label="Decorative flowing band in sand and blue tones"></div>
    <div class="contact-panel"></div>

    <h1 class="business-name">TIDAL VERGE</h1>

    <h2 class="owner-name">Darren Quellby</h2>

    <ul class="contact-list">
      <li>
        <svg class="contact-icon" viewBox="0 0 44 40" aria-hidden="true">
          <rect x="12" y="1" width="20" height="38" rx="4" fill="none" stroke="#fff" stroke-width="4"/>
          <rect x="16" y="7" width="12" height="14" fill="#fff"/>
          <circle cx="22" cy="31" r="2.5" fill="#fff"/>
        </svg>
        <span class="contact-phone">0413562049</span>
      </li>
      <li>
        <svg class="contact-icon" viewBox="0 0 44 40" aria-hidden="true">
          <rect x="2" y="7" width="40" height="26" fill="#fff"/>
          <path d="M2,7 L22,23 L42,7" fill="none" stroke="var(--brand-blue)" stroke-width="3"/>
        </svg>
        <span class="contact-email">norma.vance@fernmail.com.au</span>
      </li>
    </ul>

    <p class="free-quote">Call for free quote</p>
  </div>
</body>
</html>
```